Upbeat Accouting Package Flyer

I am looking for a 1 page (front, or front and back) flyer that will become our marketing for our accounting services. We are looking for something a little different and we are catering to the small retail shop owners. We have 3 accounting packages we would like to display and then some add-ons. I have included our logo that must be included in the design. I have uploaded the accounting package information as well.
Target Market(s)
Small Retail Shop Owners
Industry/Entity Type
Accounting
Colors
Designer to choose colors to be used in the design.
Requirements
Must have
- A casual feel. We are not your typical accountants who are very professional and "stuffy". I want it to feel like we are all family.
Nice to have
- I would like to incorporate some sort of retail theme.
- We have a couple of taglines we like to use and it would be great if they could be included. They are "We know you CAN do the accounting, but do you WANT to?" and "We allow you to get back to what's important."
Should not have
- Typical stock accounting photos of people shaking hands, large office buildings, etc.

```html
<!DOCTYPE html>
<html lang="en">
<head>
<meta charset="utf-8">
<title>Brightway Tax and Accounting – Packages Flyer</title>
<link href="https://fonts.googleapis.com/css2?family=Roboto:wght@400;700&family=Barlow+Semi+Condensed:wght@500;600&family=Barlow+Condensed:wght@600&family=Open+Sans:wght@400;700;800&family=Poppins:wght@500&display=swap" rel="stylesheet">
<style>
  :root{
    --teal:#1db5d6;
    --teal-deep:#1a7f92;
    --teal-mid:#27a8c0;
    --ink:#2f2f33;
    --text:#333;
    --panel:#efefef;
    --band:#d5d5d5;
    --footer-dark:#3a3a3d;
    --page-bg:#e9e9e9;
    --white:#fff;
  }
  *{box-sizing:border-box;margin:0;padding:0}
  html,body{width:1200px;height:1200px;overflow:hidden;background:var(--page-bg)}
  .canvas{position:relative;width:1200px;height:1200px}
  .flyer{position:absolute;left:192px;top:40px;width:868px;height:1192px;background:var(--white);
    transform:scale(.94);transform-origin:0 0;box-shadow:0 4px 18px rgba(0,0,0,.25);overflow:hidden}
  .abs{position:absolute}

  .brand{left:52px;top:62px;width:316px}
  .brand-name{font-family:'Poppins',sans-serif;font-weight:500;font-size:54px;color:var(--ink);letter-spacing:.5px;line-height:1;display:flex;align-items:center;gap:10px;white-space:nowrap}
  .brand-dot{width:14px;height:14px;border-radius:50%;background:var(--teal);flex:none}
  .brand-sub{font-family:'Poppins',sans-serif;font-weight:500;font-size:13.5px;color:var(--teal);letter-spacing:.4px;margin-top:4px;text-align:right;white-space:nowrap}

  .headline{left:46px;top:198px;font-family:'Roboto',sans-serif;color:var(--ink)}
  .headline .line{font-size:32px;line-height:38px;font-weight:400}
  .headline .accent{color:var(--teal);font-weight:700}
  .headline .ask{font-size:28px;font-weight:700;margin-top:14px}

  .cta{left:35px;top:342px;width:352px;height:43px;border-radius:6px;background:var(--teal);
    font-family:'Barlow Condensed',sans-serif;font-weight:600;font-size:21px;color:var(--white);
    display:flex;align-items:center;justify-content:center}

  .hero-photo{left:414px;top:0;width:454px;height:435px;
    background:radial-gradient(circle at 45% 60%,#b98a78 0,#8d6a62 22%,#5b5d66 55%,#c9bfbd 100%)}

  .package{width:236px}
  .package-head{position:relative;height:48px;display:flex;box-shadow:0 3px 5px rgba(0,0,0,.25);border-radius:0 6px 6px 0}
  .package-icon{width:62px;background:var(--white);display:flex;align-items:center;justify-content:center}
  .package-title{flex:1;background:linear-gradient(90deg,var(--teal-deep),var(--teal-mid));border-radius:0 6px 6px 0;
    font-family:'Roboto',sans-serif;font-weight:700;font-size:20px;color:var(--white);display:flex;align-items:center;padding-left:12px}
  .package-body{background:var(--panel);margin:0 0 0 2px;width:232px;padding:12px 6px 16px 16px;
    box-shadow:0 14px 12px -10px rgba(0,0,0,.25)}
  .package-body ul{list-style:none}
  .package-body li{position:relative;padding-left:19px;margin-bottom:7px;font-family:'Barlow Semi Condensed',sans-serif;font-weight:600;font-size:10px;line-height:14px;color:var(--text)}
  .package-body li.single{white-space:nowrap}
  .package-body li svg{position:absolute;left:0;top:2px}
  .package-body .note{font-weight:500;font-size:8px}

  .extras{left:0;top:836px;width:868px;height:241px;background:var(--band)}
  .extra-title{display:flex;align-items:center;gap:14px;font-family:'Open Sans',sans-serif;font-weight:800;font-size:18.5px;color:var(--ink)}
  .extra-text{font-family:'Open Sans',sans-serif;font-size:14.5px;line-height:18px;color:var(--text);margin-left:12px;width:760px}

  .address-bar{left:0;top:1113px;width:430px;height:57px;background:var(--teal);display:flex;align-items:center;gap:14px;padding-left:44px;
    font-family:'Barlow Semi Condensed',sans-serif;font-weight:500;font-size:14.5px;color:var(--white)}
  .footer-dark{left:0;top:1170px;width:428px;height:22px;background:var(--footer-dark)}
  .footer-teal{left:428px;top:1170px;width:440px;height:22px;background:var(--teal)}
  .contact{top:1125px;display:flex;align-items:center;gap:14px;font-family:'Open Sans',sans-serif;font-size:13.5px;color:var(--ink)}
</style>
</head>
<body>
<div class="canvas">
<div class="flyer">

  <div class="abs brand">
    <div class="brand-name"><span class="brand-dot"></span>brightway</div>
    <div class="brand-sub">TAX AND ACCOUNTING INC.</div>
  </div>

  <div class="abs headline">
    <div class="line">WE KNOW YOU CAN</div>
    <div class="line">DO THE <span class="accent">ACCOUNTING</span></div>
    <div class="ask">BUT DO YOU WANT TO?</div>
  </div>

  <div class="abs cta">We allow you to get back to what's important</div>

  <div class="abs hero-photo" role="img" aria-label="Photo of a hand holding a smartphone surrounded by connected digital icons for shopping, email and devices"></div>

  <!-- Packages -->
  <section class="abs package" style="left:50px;top:510px">
    <div class="package-head">
      <div class="package-icon"><svg width="34" height="34" viewBox="0 0 34 34" fill="none" stroke="#2f2f33" stroke-width="1.6"><path d="M4 31h26M9 31V12M5 16l4-5 4 5M19 31V6M15 10l4-5 4 5M27 31V18"/></svg></div>
      <div class="package-title">DEVELOP</div>
    </div>
    <div class="package-body">
      <ul>
        <li><svg width="11" height="11" viewBox="0 0 11 11" fill="none" stroke="#1a7f92" stroke-width="1.2"><circle cx="5.5" cy="5.5" r="4.6"/><path d="M3.2 5.6l1.6 1.6 3-3.2"/></svg>$300/mo when paid annually; $325/mo billed monthly</li>
        <li><svg width="11" height="11" viewBox="0 0 11 11" fill="none" stroke="#1a7f92" stroke-width="1.2"><circle cx="5.5" cy="5.5" r="4.6"/><path d="M3.2 5.6l1.6 1.6 3-3.2"/></svg>LedgerCloud Online subscription</li>
        <li><svg width="11" height="11" viewBox="0 0 11 11" fill="none" stroke="#1a7f92" stroke-width="1.2"><circle cx="5.5" cy="5.5" r="4.6"/><path d="M3.2 5.6l1.6 1.6 3-3.2"/></svg>Free accounting setup</li>
        <li><svg width="11" height="11" viewBox="0 0 11 11" fill="none" stroke="#1a7f92" stroke-width="1.2"><circle cx="5.5" cy="5.5" r="4.6"/><path d="M3.2 5.6l1.6 1.6 3-3.2"/></svg>Weekly transaction processing</li>
        <li class="single"><svg width="11" height="11" viewBox="0 0 11 11" fill="none" stroke="#1a7f92" stroke-width="1.2"><circle cx="5.5" cy="5.5" r="4.6"/><path d="M3.2 5.6l1.6 1.6 3-3.2"/></svg>Monthly account reconciliation <span class="note">(up to 2 accounts)</span></li>
        <li><svg width="11" height="11" viewBox="0 0 11 11" fill="none" stroke="#1a7f92" stroke-width="1.2"><circle cx="5.5" cy="5.5" r="4.6"/><path d="M3.2 5.6l1.6 1.6 3-3.2"/></svg>Monthly financial statements by the 15th of the month</li>
      </ul>
    </div>
  </section>

  <section class="abs package" style="left:318px;top:512px">
    <div class="package-head">
      <div class="package-icon"><svg width="36" height="36" viewBox="0 0 36 36" fill="none" stroke="#2f2f33" stroke-width="1.6"><circle cx="18" cy="18" r="15.5"/><path d="M9 22c4 0 6 3 9 3s6-2 9-3M18 22v-7M18 15c-3 0-5-2-5-5 3 0 5 2 5 5zM18 15c3 0 5-2 5-5-3 0-5 2-5 5z"/></svg></div>
      <div class="package-title">GROW</div>
    </div>
    <div class="package-body">
      <ul>
        <li><svg width="11" height="11" viewBox="0 0 11 11" fill="none" stroke="#1a7f92" stroke-width="1.2"><circle cx="5.5" cy="5.5" r="4.6"/><path d="M3.2 5.6l1.6 1.6 3-3.2"/></svg>$550/mo billed annually; $575/mo billed monthly</li>
        <li><svg width="11" height="11" viewBox="0 0 11 11" fill="none" stroke="#1a7f92" stroke-width="1.2"><circle cx="5.5" cy="5.5" r="4.6"/><path d="M3.2 5.6l1.6 1.6 3-3.2"/></svg>LedgerCloud Online subscription</li>
        <li><svg width="11" height="11" viewBox="0 0 11 11" fill="none" stroke="#1a7f92" stroke-width="1.2"><circle cx="5.5" cy="5.5" r="4.6"/><path d="M3.2 5.6l1.6 1.6 3-3.2"/></svg>Free accounting setup</li>
        <li><svg width="11" height="11" viewBox="0 0 11 11" fill="none" stroke="#1a7f92" stroke-width="1.2"><circle cx="5.5" cy="5.5" r="4.6"/><path d="M3.2 5.6l1.6 1.6 3-3.2"/></svg>Weekly transaction processing</li>
        <li class="single"><svg width="11" height="11" viewBox="0 0 11 11" fill="none" stroke="#1a7f92" stroke-width="1.2"><circle cx="5.5" cy="5.5" r="4.6"/><path d="M3.2 5.6l1.6 1.6 3-3.2"/></svg>Monthly account reconciliation <span class="note">(up to 4 accounts)</span></li>
        <li><svg width="11" height="11" viewBox="0 0 11 11" fill="none" stroke="#1a7f92" stroke-width="1.2"><circle cx="5.5" cy="5.5" r="4.6"/><path d="M3.2 5.6l1.6 1.6 3-3.2"/></svg>Monthly financial statements by the 10th of the month</li>
        <li><svg width="11" height="11" viewBox="0 0 11 11" fill="none" stroke="#1a7f92" stroke-width="1.2"><circle cx="5.5" cy="5.5" r="4.6"/><path d="M3.2 5.6l1.6 1.6 3-3.2"/></svg>Client portal access for document sharing</li>
      </ul>
    </div>
  </section>

  <section class="abs package" style="left:578px;top:514px">
    <div class="package-head">
      <div class="package-icon"><svg width="36" height="36" viewBox="0 0 36 36" fill="none" stroke="#2f2f33" stroke-width="1.8"><circle cx="13" cy="6" r="3"/><path d="M6 10v14h14l4 8M10 14l3 7h8M24 24h6M8 30h16"/></svg></div>
      <div class="package-title">RELAX</div>
    </div>
    <div class="package-body">
      <ul>
        <li><svg width="11" height="11" viewBox="0 0 11 11" fill="none" stroke="#1a7f92" stroke-width="1.2"><circle cx="5.5" cy="5.5" r="4.6"/><path d="M3.2 5.6l1.6 1.6 3-3.2"/></svg>$850/mo billed annually; $875/mo billed monthly</li>
        <li><svg width="11" height="11" viewBox="0 0 11 11" fill="none" stroke="#1a7f92" stroke-width="1.2"><circle cx="5.5" cy="5.5" r="4.6"/><path d="M3.2 5.6l1.6 1.6 3-3.2"/></svg>LedgerCloud Online subscription</li>
        <li><svg width="11" height="11" viewBox="0 0 11 11" fill="none" stroke="#1a7f92" stroke-width="1.2"><circle cx="5.5" cy="5.5" r="4.6"/><path d="M3.2 5.6l1.6 1.6 3-3.2"/></svg>Free accounting setup</li>
        <li><svg width="11" height="11" viewBox="0 0 11 11" fill="none" stroke="#1a7f92" stroke-width="1.2"><circle cx="5.5" cy="5.5" r="4.6"/><path d="M3.2 5.6l1.6 1.6 3-3.2"/></svg>Weekly transaction processing</li>
        <li><svg width="11" height="11" viewBox="0 0 11 11" fill="none" stroke="#1a7f92" stroke-width="1.2"><circle cx="5.5" cy="5.5" r="4.6"/><path d="M3.2 5.6l1.6 1.6 3-3.2"/></svg>Monthly account reconciliation (up to 5-10 accounts)</li>
        <li><svg width="11" height="11" viewBox="0 0 11 11" fill="none" stroke="#1a7f92" stroke-width="1.2"><circle cx="5.5" cy="5.5" r="4.6"/><path d="M3.2 5.6l1.6 1.6 3-3.2"/></svg>Monthly financial statements by the 5th of the month</li>
      </ul>
    </div>
  </section>

  <!-- Extras band -->
  <section class="abs extras">
    <div class="abs" style="left:42px;top:30px">
      <div class="extra-title">
        <svg width="28" height="28" viewBox="0 0 28 28"><circle cx="14" cy="14" r="13" fill="#2f2f33"/><circle cx="11" cy="10" r="3" fill="#1db5d6"/><path d="M6 20c0-4 2-6 5-6s5 2 5 6z" fill="#1db5d6"/><rect x="17" y="11" width="6" height="9" fill="#1db5d6"/></svg>
        CLIENT PORTAL ACCESS FOR DOCUMENT SHARING
      </div>
      <p class="extra-text" style="margin-top:14px">2 Custom Reports | Accounts Payable | Invoicing and accounts receivable | Weekly Scorecard (customized metric tracking for your business)</p>
    </div>
    <div class="abs" style="left:42px;top:129px">
      <div class="extra-title" style="gap:16px">
        <svg width="28" height="28" viewBox="0 0 28 28"><circle cx="14" cy="14" r="13" fill="#2f2f33"/><path d="M14 7v14M7 14h14" stroke="#1db5d6" stroke-width="2"/></svg>
        ADDITIONAL OPTIONS
      </div>
      <p class="extra-text" style="margin-top:10px">Payroll – 1-10 employees $85/mo; 11-30 employees $175/mo | Sales tax - $30/mo per state | Corporate taxes $50/mo | Owner taxes - $25/mo</p>
    </div>
  </section>

  <!-- Footer -->
  <div class="abs address-bar">
    <svg width="14" height="18" viewBox="0 0 14 18" fill="none" stroke="#fff" stroke-width="1.4"><path d="M7 17s-5.5-6-5.5-10a5.5 5.5 0 0 1 11 0C12.5 11 7 17 7 17z"/><circle cx="7" cy="7" r="2"/></svg>
    4410 W. Maple Avenue Lenexa, KS 66215
  </div>
  <div class="abs footer-dark"></div>
  <div class="abs footer-teal"></div>

  <div class="abs contact" style="left:446px">
    <svg width="26" height="20" viewBox="0 0 26 20" fill="none" stroke="#2f2f33" stroke-width="1.8"><rect x="1" y="3" width="24" height="15" rx="1"/><path d="M1 4l12 8 12-8"/></svg>
    hello@brightway-books.com
  </div>
  <div class="abs contact" style="left:700px">
    <svg width="20" height="20" viewBox="0 0 20 20"><path d="M4 1l4 4-2 3c1 3 3 5 6 6l3-2 4 4-3 3C8 19 1 12 1 4z" fill="#2f2f33"/></svg>
    (913) 555-0148
  </div>

</div>
</div>
</body>
</html>
```